ZEPRILO.COM is a premium domain sales company. Our competitors are companies like vastplots.example, getparcels.example, peerwords.example. Our current site is at www.zeprilos.example.

We want to have the ability to search for domains, to highlight special offers and have some testimonials on the index page.

The logo for the site is attached.

Please be sure that the order form fits on the screen without scrolling the page. I want the entire form, including the submit button to fit without any page scrolling.

Delivered product - INDEX PAGE, ORDER FORM AND CONTENT PAGE PSDs.

Target Market(s)

Small to Medium business professionals

Industry/Entity Type

It Company

Requirements
Must have
• 1. List of domains for sale
2. Simple search box with button to run the search
3. link for advanced search
4. testimonial area. Note - this can be a small box where a different testimonial is displayed on each page load.
Nice to have
• Would like the site to have some white space. Don't want a heavily packed website. Give it an "airy" feel.

```html
<!DOCTYPE html>
<html lang="en">
<head>
<meta charset="utf-8">
<title>ZEPRILO.COM – Premium Domains</title>
<link href="https://fonts.googleapis.com/css2?family=Arimo:wght@400;700&family=Ubuntu:ital,wght@0,400;0,500;0,700;1,400&display=swap" rel="stylesheet">
<style>
:root{
  --green:#2f8a2a;
  --green-dark:#2b7a1f;
  --green-light:#8cc63f;
  --lime:#7dc242;
  --blue:#1a5fa5;
  --blue-deep:#174f8c;
  --sky-top:#5d9bd3;
  --sky-bottom:#d6e6f3;
  --nav:#2b2b2b;
  --yellow:#fdc10a;
  --orange:#f7772a;
  --text:#444;
  --muted:#9a9a9a;
  --row-a:#eceeea;
  --row-b:#f6f7f4;
  --footer:#232323;
}
*{box-sizing:border-box;margin:0;padding:0}
html,body{width:1200px;height:1193px;overflow:hidden;background:#fff;font-family:"Arimo",Arial,sans-serif}
.page{position:relative;width:1200px;height:1193px}
.abs{position:absolute}

.logo{left:191px;top:24px;font-family:"Arimo",Arial,sans-serif;font-weight:700;font-size:34px;color:var(--green);letter-spacing:-.5px;display:flex;align-items:center;gap:8px}
.logo .dot{width:14px;height:14px;background:var(--green);border-radius:50%}
.phone{right:190px;top:34px;color:var(--green);font-size:16px;display:flex;align-items:center;gap:8px}

.nav{left:0;top:77px;width:1200px;height:35px;background:linear-gradient(#4a4a4a,#1e1e1e)}
.nav ul{list-style:none;display:flex;margin-left:167px;height:35px}
.nav li{color:#fff;font-size:11px;font-weight:700;padding:0 16px;line-height:35px;border-right:1px solid #555}
.nav li:first-child{padding-left:16px}

.hero{left:0;top:112px;width:1200px;height:264px;background:linear-gradient(var(--sky-top),var(--sky-bottom))}
.hero h1{position:absolute;left:195px;top:36px;font-weight:400;font-size:42px;color:#fff}
.hero .sub{position:absolute;left:198px;top:77px;font-size:12px;color:var(--blue-deep)}
.search{position:absolute;left:189px;top:101px;width:553px;height:49px;background:#fff;border:3px solid #e3e3e3;border-radius:3px;display:flex}
.search .field{flex:1;font-family:"Ubuntu",sans-serif;font-style:italic;font-size:10px;color:#666;padding:16px 11px}
.search .btn{width:104px;background:linear-gradient(#92cf3d,#5da41f);color:var(--green-dark);font-weight:700;font-size:20px;text-align:center;line-height:43px}
.adv{position:absolute;left:224px;top:150px;width:149px;height:35px;background:linear-gradient(#ffd23a,#f7b500);color:var(--green-dark);font-size:15px;text-align:center;line-height:35px;border-radius:0 0 3px 3px}
.badge{position:absolute;top:192px;height:39px;background:#fff;border:1px solid #cfcfcf;border-radius:2px}
.person{left:755px;top:57px;width:245px;height:319px;background:linear-gradient(#6e6e6e,#2c2c2c);border-radius:120px 120px 0 0}
.question{left:864px;top:77px;width:152px;height:35px;background:#6cbd2c;color:#173d08;display:flex;align-items:center;gap:8px;padding-left:14px}
.question b{font-size:12px;display:block}
.question small{font-size:9px;font-weight:700;color:#fff}
.ribbon{left:754px;top:277px;width:261px;height:88px}
.ribbon span{position:absolute;left:57px;top:30px;color:#fff;font-size:14px;line-height:17px}

.offer{left:162px;top:413px;width:853px;height:97px;background:linear-gradient(#fff 60%,#f2f4f3)}
.offer .tab{position:absolute;left:0;top:2px;width:21px;height:90px;background:var(--blue);color:#fff;font-size:9px;font-weight:700;writing-mode:vertical-rl;transform:rotate(180deg);text-align:center;letter-spacing:1px;line-height:21px;border-radius:0 2px 2px 0}
.offer .pct{position:absolute;left:49px;top:11px;font-size:33px;color:var(--lime);font-weight:400}
.offer .all{position:absolute;left:49px;top:44px;font-size:17px;color:#222;font-weight:700}
.offer .all i{color:var(--orange);font-style:normal}
.offer .divider{position:absolute;left:220px;top:4px;width:1px;height:74px;background:#ddd}
.offer .note{position:absolute;left:238px;top:29px;font-family:"Ubuntu",sans-serif;font-style:italic;font-size:17px;color:#aaa}

.tabs{left:162px;top:551px;display:flex;gap:1px}
.tabs div{height:39px;line-height:39px;color:#fff;font-size:16px;padding:0 10px}
.tabs .on{width:152px;background:var(--green)}
.tabs .off{width:167px;background:var(--blue);text-align:center}
.domains{left:162px;top:590px;width:547px;border-collapse:collapse;font-family:"Ubuntu",sans-serif;font-size:13px;color:var(--text);border-top:3px solid #52a93a}
.domains th{background:var(--green-dark);color:#a6d98b;font-style:italic;font-weight:400;text-align:left;height:38px;padding-left:12px}
.domains td{height:38.8px;padding-left:12px}
.domains tr:nth-child(odd) td{background:var(--row-a)}
.domains tr:nth-child(even) td{background:var(--row-b)}
.domains .price{color:var(--green-dark);font-weight:500}
.buy{display:inline-block;width:66px;height:20px;background:linear-gradient(#2b79c9,#1757a2);color:#fff;font-size:8px;font-weight:700;line-height:20px;text-align:center;border-radius:2px;font-family:"Arimo",Arial,sans-serif}
.viewall{left:162px;top:980px;width:547px;height:30px;background:var(--yellow);color:#222;font-family:"Ubuntu",sans-serif;font-size:13px;text-align:center;line-height:30px}

.quote{left:774px;top:588px;width:241px;height:295px;background:var(--blue);border-radius:3px;color:#fff;font-family:"Ubuntu",sans-serif;font-style:italic;font-size:12.5px;line-height:17px;text-align:center;padding:50px 26px 0}
.tail{left:804px;top:882px}
.avatar{left:775px;top:921px;width:44px;height:44px;background:linear-gradient(#c9a58a,#7a5b45);border:3px solid #fff;box-shadow:0 0 0 1px #ddd}
.author{left:830px;top:924px;font-family:"Ubuntu",sans-serif;font-size:18px;color:#555}
.author small{display:block;font-size:10px;color:var(--green-dark)}

.footer{left:0;top:1095px;width:1200px;height:98px;background:var(--footer);border-top:4px solid #1d7a3a}
.footer .links{position:absolute;left:172px;top:15px;font-family:"Ubuntu",sans-serif;font-size:10px;color:#888}
.footer .copy{position:absolute;left:172px;top:35px;font-family:"Ubuntu",sans-serif;font-size:10px;color:#888}
.social{position:absolute;left:170px;top:61px;display:flex;gap:6px}
.social span{width:21px;height:21px;border-radius:50%;background:#777}
.guarantee{position:absolute;left:623px;top:21px;width:193px;height:56px;background:var(--blue);color:#fff;display:flex;align-items:center;gap:10px;padding-left:12px}
.guarantee b{font-size:30px}
.guarantee span{font-size:12px;font-weight:700;line-height:15px}
.footlogo{position:absolute;left:920px;top:32px;font-weight:700;font-size:24px;color:#555}
</style>
</head>
<body>
<div class="page">
  <div class="abs logo"><span class="dot"></span>ZEPRILO.COM</div>
  <div class="abs phone">
    <svg width="16" height="14" viewBox="0 0 16 14"><path d="M1 4c0-2 3-3 7-3s7 1 7 3v2h-4V4H5v2H1z" fill="#222"/><rect x="3" y="7" width="10" height="6" rx="1" fill="#222"/></svg>
    +1 555.014.2297
  </div>

  <nav class="abs nav"><ul><li>HOME</li><li>ABOUT US</li><li>FAQ</li><li>TESTIMONIALS</li><li>SUPPORT</li><li>CONTACT</li></ul></nav>

  <section class="abs hero">
    <h1>Find Your Domain</h1>
    <div class="sub">You can find the best name for your business...</div>
    <div class="search"><div class="field">Start your search by entering the first character of the domain name.</div><div class="btn">Search</div></div>
    <div class="adv">Advanced Search</div>
    <div class="badge" style="left:419px;width:91px"></div>
    <div class="badge" style="left:520px;width:81px"></div>
    <div class="badge" style="left:609px;width:125px"></div>
  </section>

  <div class="abs person" role="img" aria-label="Photo of a smiling support representative in a dark suit with arms crossed"></div>
  <div class="abs question">
    <svg width="18" height="16" viewBox="0 0 18 16"><rect x="1" y="1" width="16" height="11" rx="2" fill="#fff"/><path d="M4 12l0 4 4-4z" fill="#fff"/><circle cx="6" cy="6.5" r="1" fill="#6cbd2c"/><circle cx="9" cy="6.5" r="1" fill="#6cbd2c"/><circle cx="12" cy="6.5" r="1" fill="#6cbd2c"/></svg>
    <div><b>Got A Question?</b><small>Get LIVE Support</small></div>
  </div>
  <div class="abs ribbon">
    <svg width="261" height="88" viewBox="0 0 261 88"><path d="M46 0 0 44 46 88V70H261V24L247 0V24H46z" fill="var(--orange)"/><rect x="58" y="26" width="199" height="42" fill="none" stroke="#ffc08a" stroke-width="1" stroke-dasharray="2 2"/></svg>
    <span>Most Popular<br>Premium Domain Seller</span>
  </div>

  <section class="abs offer">
    <div class="tab">SPECIAL OFFER</div>
    <div class="pct">20% OFF</div>
    <div class="all">ON ALL DOMAIN<i>*</i></div>
    <div class="divider"></div>
    <div class="note">Get 30% OFF on All Domain just for Today. HUrry Up. Place Your Order Now.</div>
  </section>

  <div class="abs tabs"><div class="on">Domains For SALE</div><div class="off">Domains Categories</div></div>
  <table class="abs domains">
    <tr><th style="width:209px">Domains</th><th style="width:144px">Category</th><th style="width:107px">Price</th><th>Action</th></tr>
    <tr><td>remedyline.example</td><td>Health</td><td class="price">$8700.00</td><td><span class="buy">BUY NOW ▸</span></td></tr>
    <tr><td>trainerpouch.example</td><td>Sports</td><td class="price">$5000.00</td><td><span class="buy">BUY NOW ▸</span></td></tr>
    <tr><td>vintage-wheels.example</td><td>Vehicles</td><td class="price">$100.00</td><td><span class="buy">BUY NOW ▸</span></td></tr>
    <tr><td>freshmotors.example</td><td>Vehicles</td><td class="price">$100.00</td><td><span class="buy">BUY NOW ▸</span></td></tr>
    <tr><td>sonidovault.example</td><td>Other</td><td class="price">$4397.00</td><td><span class="buy">BUY NOW ▸</span></td></tr>
    <tr><td>everyhomestead.example</td><td>Real Estate</td><td class="price">$999.00</td><td><span class="buy">BUY NOW ▸</span></td></tr>
    <tr><td>daily-brief.example</td><td>Media</td><td class="price">$197.00</td><td><span class="buy">BUY NOW ▸</span></td></tr>
    <tr><td>fabricaproceso.example</td><td>Law</td><td class="price">$100.00</td><td><span class="buy">BUY NOW ▸</span></td></tr>
    <tr><td>ledgerrelief.example</td><td>Finance</td><td class="price">$300.00</td><td><span class="buy">BUY NOW ▸</span></td></tr>
  </table>
  <div class="abs viewall">VIEW ALL DOMAINS ➡</div>

  <blockquote class="abs quote">Lorem ipsum dolor sit amet, consectetur adipiscing elit. Mauris congue, ante ut rutrum consectetur, quam ipsum euismod libero, vel rhoncus augue ipsum quis purus. Quisque interdum, nisl eu dictum congue, lacus sem porttitor enim, commodo hendrerit turpis orci in diam.</blockquote>
  <svg class="abs tail" width="24" height="25" viewBox="0 0 24 25"><path d="M0 0H24L2 25z" fill="var(--blue)"/></svg>
  <div class="abs avatar" role="img" aria-label="Customer portrait"></div>
  <div class="abs author">Dana Whitlow<small>USA</small></div>

  <footer class="abs footer">
    <div class="links">Home &nbsp;|&nbsp; About &nbsp;|&nbsp; Support &nbsp;|&nbsp; Privacy &nbsp;|&nbsp; Terms &amp; Conditions &nbsp;|&nbsp; Testimonials</div>
    <div class="copy">© 2013 Zeprilo.com. All rights reserved.</div>
    <div class="social"><span></span><span></span><span></span><span></span></div>
    <div class="guarantee"><b>100%</b><span>SATISFACTION<br>GUARANTEED</span></div>
    <div class="footlogo">ZEPRILO.COM</div>
  </footer>
</div>
</body>
</html>
```